Business Card Design Project

I am looking for a classy business card design for a product design consultancy. We specialize in Product Design, Prototyping, and Manufacturing Consulting. Products that we design range from consumer electronics to household products all the way to sporting goods. We are based in Arizona and called "Heron Design Works." We like to have fun and goof off as much as we like to create new products. We are young and energetic so we would like our business cards to reflect that. We already have a logo that we would like to implement into the card design. A plain rectangular business card is boring so feel free to get creative, but please, no avocado shaped cards (it's far too literal). Also feel free to play around with textured card stocks or plastic. The final design that we choose will pay attention to all of the little details. Our cards will need to be 2 sided. We're giving you guys free reign to design as you would like. Please have fun with this, it will reflect in our business card.

Thanks guys,
Heron Design Works Team

Industry/Entity Type

Electronics

Requirements
Must have
• We would like to have a spot UV coating somewhere on the business card design if possible.
Nice to have
• Let's see some designs with custom shapes rather than typical rectangular business cards but please no avocado shaped cards, thanks. Also play around with textured card socks.

```html
<!DOCTYPE html>
<html lang="en">
<head>
<meta charset="utf-8">
<title>Heron Design Works – Business Card</title>
<link rel="stylesheet" href="https://fonts.googleapis.com/css2?family=Arimo:wght@400;700&display=swap">
<style>
  :root {
    --page-bg: #ffffff;
    --front-frame: #e6e6e7;
    --front-panel: #f1f1f2;
    --brand-green: #8cc63f;
    --info-grey: #bcbdbf;
    --text-grey: #6d6e71;
    --text-white: #ffffff;
  }
  html, body {
    margin: 0;
    padding: 0;
    width: 1200px;
    height: 684px;
    overflow: hidden;
    background: var(--page-bg);
  }
  .card-sheet {
    display: block;
    width: 1200px;
    height: 684px;
    font-family: "Arimo", Arial, sans-serif;
  }
  .front-frame { fill: var(--front-frame); }
  .front-panel { fill: var(--front-panel); }
  .brand-mark { fill: var(--brand-green); }
  .brand-name {
    fill: var(--brand-green);
    font-size: 36px;
    font-weight: 400;
    letter-spacing: 0.5px;
  }
  .back-base { fill: var(--brand-green); }
  .info-panel { fill: var(--info-grey); }
  .info-label {
    fill: var(--text-white);
    font-size: 16px;
    font-weight: 400;
  }
  .info-value {
    fill: var(--text-white);
    font-size: 12px;
    font-weight: 400;
  }
  .holder-name {
    fill: var(--text-grey);
    font-size: 21px;
    font-weight: 700;
  }
  .holder-title {
    fill: var(--text-grey);
    font-size: 16px;
    font-weight: 400;
  }
</style>
</head>
<body>
<svg class="card-sheet" viewBox="0 0 1200 684" xmlns="http://www.w3.org/2000/svg">
  <defs>
    <linearGradient id="dotFieldTone" x1="0" y1="0" x2="1" y2="0">
      <stop offset="0" stop-color="#8cc63f"/>
      <stop offset="0.55" stop-color="#a9d46e"/>
      <stop offset="1" stop-color="#b4b6b8"/>
    </linearGradient>
    <linearGradient id="wavePatternTone" x1="0" y1="0" x2="1" y2="0">
      <stop offset="0" stop-color="#a7a9ac" stop-opacity="0"/>
      <stop offset="0.5" stop-color="#a7a9ac" stop-opacity="0.35"/>
      <stop offset="1" stop-color="#a7a9ac" stop-opacity="0.1"/>
    </linearGradient>
  </defs>

  <g class="card-front">
    <path class="front-frame" d="M82 192 H569 V483 H82 A25 25 0 0 1 57 458 V217 A25 25 0 0 1 82 192 Z"/>
    <rect class="front-panel" x="82" y="217" width="470" height="244" rx="40"/>
    <rect x="511" y="194" width="58" height="286" fill="url(#dotFieldTone)" opacity="0.85"
          role="img" aria-label="Decorative halftone dot field in green and grey"/>
    <circle class="brand-mark" cx="124" cy="333" r="20"/>
    <text class="brand-name" x="156" y="346">Heron Design Works</text>
  </g>

  <g class="card-back">
    <path class="back-base" d="M617 190 H1106 A25 25 0 0 1 1131 215 V458 A25 25 0 0 1 1106 483 H617 Z"/>
    <path class="info-panel" d="M665 215 H792 L878 336 L792 455 H665 A30 30 0 0 1 635 425 V245 A30 30 0 0 1 665 215 Z"/>

    <rect x="840" y="206" width="269" height="103" fill="url(#wavePatternTone)"
          role="img" aria-label="Decorative halftone wave pattern in grey"/>
    <rect x="846" y="366" width="257" height="103" fill="url(#wavePatternTone)"
          role="img" aria-label="Decorative halftone wave pattern in grey"/>

    <text class="info-label" x="648" y="261">Phone</text>
    <text class="info-value" x="652" y="285">Office: 480.555.0142</text>
    <text class="info-value" x="652" y="308">Cell: 602.555.0187</text>

    <text class="info-label" x="648" y="343">Email</text>
    <text class="info-value" x="652" y="367">dylan@herondesignworks.com</text>

    <text class="info-label" x="648" y="401">Web</text>
    <text class="info-value" x="652" y="422">www.herondesignworks.com</text>

    <text x="896" y="344"><tspan class="holder-name">Dylan Marsh</tspan><tspan class="holder-title" dx="7">• President</tspan></text>
  </g>
</svg>
</body>
</html>
```